The Velvet Needle Poster for a shop Facade

Hello Designers,

• We have a 4X4 meters façade for our tailor shop “The Velvet Needle”, and we are looking for a unique, simple and attractive poster to be printed on the glass to attract the attention of the driving customers or whoever passes by the shop.
• The Velvet Needle, with ‘Velvet’ referring to door-to-door service, our concept as follows (Call … Measure … Stitch … Deliver)

1. Step1: Book online or simply call us to make your appointment (should be pictorial not writing)
2. Step2: Our dedicated personnel will come to you at your preferred time and location. (should be pictorial not writing)
3. Step3: Clothes Alteration/Making to suit your style and body fit. (should be pictorial not writing)
4. Step4: Delivery on completion, at your preferred time and location. (should be pictorial not writing)

• We are specialized in clothes alteration and making for both men and women, and anything related to tailoring services www.thevelvetneedle.example

• The poster must include the name “The Velvet Needle” as well as the phone number 04 318 2976 in a very clear and obvious way (logo will be optional if you can show it in a nice way)
And the concept of our shop should be shown in the poster in a very simple and clear way and more graphical than words. (Perhaps a graphical flow to show client booking our service and we go to their place for alterations done).
Colors should be chosen carefully to attract the customers and the walk-ins eyes when they pass by either walking or by cars.

Thank you
Omar

Target Market(s)

We have a 4X4 meters façade for our tailor shop “The Velvet Needle”, and we are looking for a unique, simple and attractive poster to be printed on the glass to attract the attention of the driving customers or whoever passes by the shop.

Industry/Entity Type

Fashion

• to match the poster/signage

Colors

Designer to choose colors to be used in the design.

Requirements
Must have
Nice to have
• the concept of our shop should be shown in the poster in a very simple and clear way and more graphical than words. (Perhaps a graphical flow to show client booking our service and we go to their place for alterations done).
Should not have
• many words, copied designs. Please only use the images attached in the project brief for reference.

```html
<!DOCTYPE html>
<html lang="en">
<head>
<meta charset="utf-8">
<title>The Velvet Needle – Facade Poster</title>
<link href="https://fonts.googleapis.com/css2?family=Montserrat:wght@300;400;600&display=swap" rel="stylesheet">
<style>
  :root {
    --panel-top: #3d3d3d;
    --panel-bottom: #353535;
    --ink-light: #ffffff;
    --ink-dark: #1e1e1e;
    --icon-ink: #2e2e2e;
    --muted: #d8d8d8;
  }
  * { margin: 0; padding: 0; box-sizing: border-box; }
  html, body { width: 1200px; height: 1200px; overflow: hidden; }
  body {
    background: linear-gradient(180deg, var(--panel-top), var(--panel-bottom));
    font-family: "Montserrat", sans-serif;
    color: var(--ink-light);
    position: relative;
  }
  .frame {
    position: absolute;
    left: 37px; top: 37px; right: 37px; bottom: 37px;
    border: 2px solid var(--ink-light);
    border-radius: 40px;
  }
  .brand-badge {
    position: absolute;
    left: 364px; top: 100px;
    width: 472px; height: 472px;
    border-radius: 50%;
    border: 3px solid var(--ink-light);
    display: flex; align-items: center; justify-content: center;
  }
  .brand-badge__disc {
    width: 446px; height: 446px;
    border-radius: 50%;
    background: var(--ink-light);
    color: var(--ink-dark);
    display: flex; flex-direction: column; align-items: center; justify-content: center;
    text-align: center;
  }
  .brand-name {
    font-weight: 300;
    font-size: 52px;
    line-height: 1.15;
    letter-spacing: 1px;
  }
  .brand-tagline {
    margin-top: 60px;
    font-weight: 300;
    font-size: 15px;
    letter-spacing: 5px;
    line-height: 1.5;
  }
  .specialty {
    position: absolute;
    left: 241px; width: 718px; top: 617px;
    border-top: 1.5px solid var(--muted);
    border-bottom: 1.5px solid var(--muted);
    padding: 6px 0 7px;
    text-align: center;
    font-weight: 300;
    font-size: 23px;
    line-height: 1.2;
    letter-spacing: 0.5px;
  }
  .process {
    position: absolute;
    left: 0; top: 728px;
    width: 1200px; height: 220px;
  }
  .process svg { display: block; }
  .step-label {
    position: absolute;
    top: 168px;
    width: 200px;
    text-align: center;
    font-weight: 400;
    font-size: 25px;
    letter-spacing: 7px;
  }
  .divider {
    position: absolute;
    left: 485px; top: 975px;
    width: 228px; height: 2px;
    background: var(--ink-light);
  }
  .phone-line {
    position: absolute;
    left: 0; width: 1200px; top: 1004px;
    text-align: center;
    font-weight: 300;
    font-size: 62px;
    letter-spacing: 1px;
  }
  .web-line {
    position: absolute;
    left: 0; width: 1200px; top: 1082px;
    text-align: center;
    font-weight: 300;
    font-size: 19px;
    letter-spacing: 1px;
    color: var(--muted);
  }
  .web-line strong { font-weight: 600; color: var(--ink-light); }
</style>
</head>
<body>
  <div class="frame"></div>

  <div class="brand-badge">
    <div class="brand-badge__disc">
      <div class="brand-name">The Velvet<br>Needle</div>
      <div class="brand-tagline">Clothes<br>Alterations</div>
    </div>
  </div>

  <div class="specialty">SPECIALIZED IN CLOTHES ALTERATION AND MAKING<br>FOR BOTH MEN AND WOMEN</div>

  <div class="process">
    <svg width="1200" height="160" viewBox="0 0 1200 160">
      <defs>
        <radialGradient id="step-art" cx="50%" cy="50%" r="50%">
          <stop offset="0%" stop-color="#2e2e2e"/>
          <stop offset="60%" stop-color="#5a5a5a"/>
          <stop offset="100%" stop-color="#bdbdbd"/>
        </radialGradient>
      </defs>
      <g fill="none" stroke="#ffffff" stroke-width="2">
        <circle cx="267" cy="80" r="73"/>
        <circle cx="489" cy="80" r="73"/>
        <circle cx="711" cy="80" r="73"/>
        <circle cx="933" cy="80" r="73"/>
      </g>
      <g fill="#ffffff">
        <circle cx="267" cy="80" r="65"/>
        <circle cx="489" cy="80" r="65"/>
        <circle cx="711" cy="80" r="65"/>
        <circle cx="933" cy="80" r="65"/>
      </g>
      <!-- call step: phone icon -->
      <g class="icon-phone" fill="#2e2e2e">
        <path d="M238 58c4-4 9-4 12 0l7 10c2 3 2 7-1 10l-5 4c3 8 10 15 18 19l4-5c3-3 7-3 10-1l10 7c4 3 4 8 0 12l-6 6c-4 4-10 5-16 3-20-8-35-23-43-43-2-6-1-12 3-16z"/>
      </g>
      <g class="icon-waves" fill="none" stroke="#2e2e2e" stroke-width="6" stroke-linecap="round">
        <path d="M270 64a14 14 0 0 1 14 14"/>
        <path d="M272 48a30 30 0 0 1 30 30"/>
      </g>
      <!-- remaining steps: picture areas -->
      <circle class="step-art step-art--measure" cx="489" cy="80" r="50" fill="url(#step-art)" role="img" aria-label="Picture: tailor measuring a standing client with a tape"/>
      <circle class="step-art step-art--stitch" cx="711" cy="80" r="50" fill="url(#step-art)" role="img" aria-label="Picture: needle and thread stitching along a seam line"/>
      <circle class="step-art step-art--deliver" cx="933" cy="80" r="50" fill="url(#step-art)" role="img" aria-label="Picture: open hand handing over a parcel"/>
      <!-- flow arrows -->
      <g fill="none" stroke="#ffffff" stroke-width="3">
        <g transform="translate(364 80)"><path d="M0-12 8 0 0 12M9-12 17 0 9 12M18-12 26 0 18 12"/></g>
        <g transform="translate(587 80)"><path d="M0-12 8 0 0 12M9-12 17 0 9 12M18-12 26 0 18 12"/></g>
        <g transform="translate(809 80)"><path d="M0-12 8 0 0 12M9-12 17 0 9 12M18-12 26 0 18 12"/></g>
      </g>
    </svg>
    <div class="step-label" style="left:167px">CALL</div>
    <div class="step-label" style="left:389px">MEASURE</div>
    <div class="step-label" style="left:611px">STITCH</div>
    <div class="step-label" style="left:833px">DELIVER</div>
  </div>

  <div class="divider"></div>

  <div class="phone-line">CALL US: 04 318 2976</div>
  <div class="web-line">FOR TAILORING SERVICES VISIT <strong>WWW.THEVELVETNEEDLE.EXAMPLE</strong></div>
</body>
</html>
```